Business cards for a new business: Willow Brook Calm Healing

I would like for the card to include a lotus. The business is a healing practice so I'd like the overall colours to be pink and green and for it to have a soft feel. The name of the practice is
"Willow Brook Calm Healing", which I'd like to be included, as well as the words: "Energetic and spiritual healing to restore health, harmony and wellbeing". Also, my name - Tarik and the number: 5391 6048

Target Market(s)

Everyone interested in personal healing!

Industry/Entity Type

Business

Contact Information for Business Card

As above……..could be single or double-sided
I'd like the font for the name of the practice and my name to be in green and be a flowing, but simple font - elegant.
The background to be a light pink. See below for colours

Colors
f9d9e8
eea4c8
e567a6
d0ebe7
86cfc6
33b7a4

Requirements
Must have
• See above
Nice to have
• See above

```html
<!DOCTYPE html>
<html lang="en">
<head>
<meta charset="utf-8">
<title>Willow Brook Calm Healing – Business Cards</title>
<link rel="stylesheet" href="https://fonts.googleapis.com/css2?family=Marcellus&display=swap">
<style>
  :root {
    --page: #ffffff;
    --card-edge: #6f6f6f;
    --teal-light: #a2d6d3;
    --teal-mid: #5fa8a6;
    --teal-deep: #1b6764;
    --teal-dark: #0f5a58;
    --ink-green: #17625f;
    --ink-light: #ffffff;
    --pink-bright: #e567a6;
    --pink-soft: #eea4c8;
  }
  * { box-sizing: border-box; margin: 0; padding: 0; }
  html, body {
    width: 1200px;
    height: 927px;
    overflow: hidden;
    background: var(--page);
  }
  .canvas {
    position: relative;
    width: 1200px;
    height: 927px;
  }
  .card {
    position: absolute;
    top: 130px;
    width: 380px;
    height: 664px;
    border: 1px solid var(--card-edge);
    overflow: hidden;
  }
  .card--front {
    left: 188px;
    background: linear-gradient(
      to bottom,
      var(--teal-light) 0%,
      var(--teal-light) 50%,
      var(--teal-mid) 66%,
      var(--teal-deep) 88%,
      var(--teal-dark) 100%
    );
    font-family: "Marcellus", "Optima", serif;
    text-align: center;
  }
  .card--back { left: 617px; }
  .card--back svg {
    display: block;
    width: 100%;
    height: 100%;
  }

  .brand__name {
    position: absolute;
    left: 0;
    width: 100%;
    color: var(--ink-green);
    font-weight: 400;
    line-height: 1;
  }
  .brand__name--top {
    top: 62px;
    font-size: 46px;
    letter-spacing: 0.5px;
  }
  .brand__name--bottom {
    top: 300px;
    font-size: 30px;
    letter-spacing: 1px;
  }
  .brand__mark {
    position: absolute;
    top: 140px;
    left: 125px;
    width: 130px;
    height: 130px;
    border-radius: 50%;
    background: radial-gradient(circle,
      var(--pink-bright) 0%,
      var(--pink-soft) 22%,
      var(--teal-deep) 42%,
      var(--teal-mid) 70%,
      var(--teal-light) 100%);
  }

  .tagline {
    position: absolute;
    top: 428px;
    left: 0;
    width: 100%;
    color: var(--ink-light);
    font-size: 26px;
    line-height: 37px;
  }
  .contact {
    position: absolute;
    top: 562px;
    left: 0;
    width: 100%;
    color: var(--ink-light);
    font-size: 24px;
    line-height: 38px;
  }
  .contact__phone { letter-spacing: 1.5px; }
</style>
</head>
<body>
  <main class="canvas">
    <section class="card card--front" aria-label="Business card front">
      <h1 class="brand">
        <span class="brand__name brand__name--top">Willow Brook</span>
        <span class="brand__name brand__name--bottom">Calm Healing</span>
      </h1>
      <div class="brand__mark" aria-hidden="true"></div>
      <p class="tagline">Energetic and spiritual<br>healing to restore health,<br>harmony and wellbeing.</p>
      <div class="contact">
        <p class="contact__name">Tarik</p>
        <p class="contact__phone">5391 6048</p>
      </div>
    </section>

    <section class="card card--back" aria-label="Business card back">
      <svg viewBox="0 0 380 664" role="img" aria-label="Large soft teal flower with a pink centre">
        <defs>
          <radialGradient id="back-glow" gradientUnits="userSpaceOnUse" cx="190" cy="300" r="360">
            <stop offset="0%" stop-color="#e567a6"/>
            <stop offset="14%" stop-color="#e98fbf"/>
            <stop offset="22%" stop-color="#1b6764"/>
            <stop offset="55%" stop-color="#4e9e9c"/>
            <stop offset="100%" stop-color="#a2d6d3"/>
          </radialGradient>
        </defs>
        <rect width="380" height="664" fill="url(#back-glow)"/>
      </svg>
    </section>
  </main>
</body>
</html>
```